Corwick Habitat Web

We just need an update/re-design of our existing web site that would include our new company logo and some new photo's. Our current web site can be viewed at www.corwickhabitat.com.au. We would require something very similar to what we have at the moment in terms of content it should all be the same.
The web site would basically act more as a portfolio than one that would generate more business.
We are after a very modern and simple design and maybe something where we can upload our own project photo's and project descriptions as we complete them.

Industry/Entity Type

It Company

```html
<!DOCTYPE html>
<html lang="en">
<head>
<meta charset="utf-8">
<title>Corwick Habitat</title>
<link rel="stylesheet" href="https://fonts.googleapis.com/css2?family=Cinzel:wght@400;500&family=Open+Sans:wght@400;600&family=Roboto+Condensed:wght@400&family=Quicksand:wght@300&display=swap">
<style>
:root{
  --paper:#eeeeeb;
  --steel:#4a7591;
  --ink:#222222;
  --body-ink:#3a3a3a;
  --logo-grey:#6d6d6d;
  --white:#ffffff;
  --night:#000000;
}
*{box-sizing:border-box;margin:0;padding:0}
html,body{width:1200px;height:1101px;overflow:hidden}
body{position:relative;background:var(--paper);font-family:"Open Sans",sans-serif;color:var(--body-ink)}
.brand{position:absolute;left:128px;top:22px;font-family:"Quicksand",sans-serif;font-weight:300;font-size:40px;color:var(--logo-grey);letter-spacing:-0.5px;line-height:1}
.nav-bar{position:absolute;left:0;top:85px;width:1200px;height:38px;background:var(--steel)}
.nav{position:absolute;left:126px;top:0;display:flex;height:38px;list-style:none}
.nav li{font-family:"Roboto Condensed",sans-serif;font-size:11px;letter-spacing:1px;color:var(--white);line-height:38px;padding:0 28px 0 10px;position:relative}
.nav li+li{padding-left:29px}
.nav li+li::before{content:"";position:absolute;left:0;top:7px;width:1px;height:24px;background:rgba(255,255,255,.35)}
.search{position:absolute;left:876px;top:7px;width:194px;height:24px;background:var(--white);border-radius:4px;font-family:Georgia,serif;font-style:italic;font-size:11px;color:#aaa;line-height:24px;padding-left:12px}
.search svg{position:absolute;right:9px;top:6px}
.hero{position:absolute;left:126px;top:123px;width:947px;height:515px;background:linear-gradient(180deg,#2d2f33 0%,#6e6660 28%,#d9d6d0 55%,#b9b3a6 80%,#8d8676 100%)}
.hero-caption{position:absolute;left:0;top:212px;width:947px;height:95px;background:rgba(255,255,255,.78);text-align:center;font-family:"Cinzel",serif;color:var(--ink)}
.hero-caption h1{font-weight:400;font-size:26px;letter-spacing:1px;margin-top:20px;margin-left:グ0}
.hero-caption p{font-size:15px;margin-top:2px;letter-spacing:.5px}
.hero-arrow{position:absolute;top:248px}
.intro{position:absolute;left:128px;top:662px;width:590px}
.intro h2{font-family:Arial,Helvetica,sans-serif;font-weight:400;font-size:20px;color:var(--ink);margin-bottom:14px}
.intro p,.intro li{font-size:12.5px;line-height:21px;padding-left:3px}
.intro ul{list-style:none;padding-left:22px}
.intro li{font-weight:600;color:var(--ink)}
.intro li::before{content:">  ";white-space:pre}
.projects{position:absolute;left:742px;top:638px;width:331px;height:375px;background:var(--steel)}
.projects h3{font-family:Arial,Helvetica,sans-serif;font-weight:400;font-size:20px;color:var(--white);position:absolute;left:18px;top:26px}
.thumb{position:absolute;left:21px;width:290px;height:73px;border:2px solid #d8dde0}
.thumb-featured{top:67px;background:linear-gradient(90deg,#3a3a3a,#5b5b5b 60%,#4a4a4a);text-align:center;color:var(--white)}
.thumb-featured strong{display:block;font-weight:600;font-size:13px;margin-top:19px}
.thumb-featured span{font-size:11px;font-weight:600}
.thumb-facade{top:150px;background:linear-gradient(180deg,#9fc3e2 0%,#5d7e9a 45%,#3b4650 75%,#8b4a2e 100%)}
.thumb-building{top:234px;background:linear-gradient(180deg,#a7bfd6 0%,#6b6a68 40%,#b4643a 65%,#cfcfcf 100%)}
.more{position:absolute;left:138px;top:322px;width:56px;border-top:1px solid rgba(255,255,255,.7);text-align:center;font-family:"Roboto Condensed",sans-serif;font-size:11px;color:var(--white);letter-spacing:1px;padding-top:11px}
.footer{position:absolute;left:0;top:1013px;width:1200px;height:88px;background:var(--night)}
.footer-brand{position:absolute;left:131px;top:28px;font-family:"Quicksand",sans-serif;font-weight:300;font-size:21px;color:#8a8a8a}
.footer-contact{position:absolute;right:139px;top:23px;text-align:right;font-size:10px;line-height:15px;color:var(--white)}
</style>
</head>
<body>
<header>
  <div class="brand">Corwick Habitat</div>
  <div class="nav-bar">
    <ul class="nav">
      <li>HOME</li><li>RECENT PROJECTS</li><li>OUR SERVICES</li><li>CONTACT US</li>
    </ul>
    <div class="search">Search
      <svg width="12" height="12" viewBox="0 0 12 12"><circle cx="5" cy="5" r="3.6" fill="none" stroke="#bbb" stroke-width="1.6"/><line x1="7.6" y1="7.6" x2="11" y2="11" stroke="#bbb" stroke-width="2"/></svg>
    </div>
  </div>
</header>

<section class="hero" role="img" aria-label="Photo of a fitted-out office lobby with timber ceiling battens, glass stair and patterned carpet">
  <div class="hero-caption">
    <h1>Comfort within your grasp</h1>
    <p>See more</p>
  </div>
  <svg class="hero-arrow" style="left:14px" width="24" height="24" viewBox="0 0 24 24"><circle cx="12" cy="12" r="11" fill="#111" stroke="#fff" stroke-width="1.5"/><path d="M14 7l-5 5 5 5" fill="none" stroke="#fff" stroke-width="2.4"/></svg>
  <svg class="hero-arrow" style="left:912px" width="24" height="24" viewBox="0 0 24 24"><circle cx="12" cy="12" r="11" fill="#111" stroke="#fff" stroke-width="1.5"/><path d="M10 7l5 5-5 5" fill="none" stroke="#fff" stroke-width="2.4"/></svg>
</section>

<main class="intro">
  <h2>Corwick Habitat Pty Limited</h2>
  <p>Corwick Habitat Pty Ltd was established in 2005 and has been operating in the Sydney area, but has completed numerous projects outside of Sydney.<br>We specialise in the internal fit outs to,</p>
  <ul>
    <li>Industrial Offices</li>
    <li>Multi Storey Offices</li>
    <li>Commercial Projects</li>
    <li>Residential Houses</li>
    <li>External Facades</li>
  </ul>
  <p>The key group of our operating staff have all been involved in the construction industry for well over 20 years.&nbsp; Our employees are skilled and trained and have the experience to deliver the best possible product, safely and on time. At Corwick Habitat we pride ourselves on working together with our clients in providing the best possible service on schedule and within budget</p>
</main>

<aside class="projects">
  <h3>Recent Projects</h3>
  <div class="thumb thumb-featured" role="img" aria-label="Project photo of a building entrance"><strong>Harbourside Pavilion</strong><span>[ Read more ]</span></div>
  <div class="thumb thumb-facade" role="img" aria-label="Project photo of a glazed office facade"></div>
  <div class="thumb thumb-building" role="img" aria-label="Project photo of a commercial building exterior"></div>
  <div class="more">MORE</div>
</aside>

<footer class="footer">
  <div class="footer-brand">Corwick Habitat</div>
  <address class="footer-contact" style="font-style:normal">
    418 Larkfield Road, Marrowvale<br>
    Tel: 0800-462-117, 1800-519-330<br>
    Email: info@corwickhabitat.com
  </address>
</footer>
</body>
</html>
```